Modern Label for cleaning products for the brand Voralux

We need a label design for our line of cleaning products. The label should feature our logo and an image to identify the product's intended use. I've added our logo and an image for use. This only concerns the design of the label on the front of the bottle.

Label dimensions:
Label 1 (500ml bottle with spray): width 58mm x height 115mm
Label 2: (1L bottle): width 73mm x height 140mm
The design must be consistent for both bottles which you find in the pictures.

The bottles to be labeled are white. See the attachment for a photo of the bottles.

The photo must also appear on the label to identify the product's intended use.

Product information:
Brand: Voralux
Product: Sanitary Cleaner

This text must be placed on the label:
"Cleans, descales & freshens. followed with this text: "Ideal for quick and powerful cleaning. A ready-to-use product for everyday use."

- Mention the seperate USP's: Sanitary, Bathroom, Toilet, Wet areas

Appearance: This is a consumer product, but it must have a professional appearance. We would like to see a design that use the color blue from our logo.

Target Market(s)

Consumers who take care of their homes and want to maintain it the correct (professional) way

Font styles to use
Sans Serif

Colors
0054AA
0677BA
7BADD7
CADEEF
E8F1F8

Requirements
Must have
• USP's + use of image and logo + blend in 1 design
Nice to have
• Keep the color of the logo in the design
Should not have
• Comic sans

```html
<!DOCTYPE html>
<html lang="en">
<head>
<meta charset="utf-8">
<title>Voralux Sanitary Cleaner – Front Labels</title>
<link href="https://fonts.googleapis.com/css2?family=Montserrat:wght@400;500;600;700;800&display=swap" rel="stylesheet">
<style>
  :root{
    --brand-blue:#0054AA;
    --mid-blue:#0677BA;
    --soft-blue:#7BADD7;
    --pale-blue:#CADEEF;
    --mist-blue:#E8F1F8;
    --white:#ffffff;
    --stage:#9c9db9;
    --ink:#2c4a6e;
  }
  *{box-sizing:border-box;margin:0;padding:0}
  html,body{width:742px;height:1200px;overflow:hidden}
  body{
    background:var(--stage);
    font-family:'Montserrat',sans-serif;
    display:flex;align-items:center;justify-content:center;
  }
  .label-set{display:flex;align-items:flex-end;gap:30px}
  .label-slot{display:flex;flex-direction:column;align-items:center;gap:8px}
  .label-caption{font-size:10px;font-weight:600;color:#3a3c5a}
  .label{
    position:relative;overflow:hidden;background:var(--white);
    border-radius:.6em;
    box-shadow:0 0 0 1px rgba(0,84,170,.25);
  }
  .label--500{width:290px;height:575px;font-size:10px}
  .label--1l{width:365px;height:700px;font-size:12.6px}
  .label__art{position:absolute;inset:0;width:100%;height:100%}
  .brand{
    position:absolute;top:3.5%;left:0;right:0;
    display:flex;flex-direction:column;align-items:center;gap:.35em;
    color:var(--white);
  }
  .brand__dot{width:2.4em;height:2.4em;border-radius:50%;background:var(--white)}
  .brand__name{font-size:1.35em;font-weight:700;letter-spacing:.02em}
  .product-name{
    position:absolute;top:12.8%;left:0;right:0;text-align:center;
    color:var(--white);font-weight:800;line-height:1.05;font-size:1em;
  }
  .product-name__line{display:block;font-size:3.4em;letter-spacing:.02em}
  .claim{
    position:absolute;top:65.5%;left:0;right:0;text-align:center;
    color:var(--brand-blue);font-weight:800;font-size:1.2em;letter-spacing:.02em;
  }
  .usp-list{
    position:absolute;top:71%;left:8%;right:8%;
    display:flex;justify-content:space-between;list-style:none;
  }
  .usp{display:flex;flex-direction:column;align-items:center;gap:.35em;width:24%}
  .usp svg{width:2.6em;height:2.6em}
  .usp__text{font-size:.62em;font-weight:700;color:var(--brand-blue);text-transform:uppercase;text-align:center;white-space:nowrap}
  .description{
    position:absolute;top:83%;left:14%;right:14%;text-align:center;
    color:var(--ink);font-size:.82em;font-weight:500;line-height:1.4;
  }
</style>
</head>
<body>
<main class="label-set">

  <section class="label-slot">
    <p class="label-caption">500ml bottle</p>
    <article class="label label--500">
      <svg class="label__art" viewBox="0 0 100 100" preserveAspectRatio="none" aria-hidden="true">
        <defs>
          <linearGradient id="photo500" x1="0" y1="0" x2="1" y2="1">
            <stop offset="0" stop-color="#d9dcdf"/><stop offset=".45" stop-color="#f3f4f4"/>
            <stop offset=".75" stop-color="#8d8f92"/><stop offset="1" stop-color="#5a5d62"/>
          </linearGradient>
        </defs>
        <path d="M0 0H100V31Q50 25 0 32Z" fill="var(--brand-blue)"/>
        <path d="M0 58Q50 64 100 57V61Q50 67 0 62Z" fill="var(--mid-blue)"/>
        <path d="M0 57Q50 63 100 56V58Q50 64 0 59Z" fill="var(--soft-blue)"/>
      </svg>
      <svg class="label__art" viewBox="0 0 100 100" preserveAspectRatio="none" role="img" aria-label="Photo of a clean modern bathroom with shower and washbasin">
        <path d="M0 32Q50 25 100 31V56Q50 63 0 57Z" fill="url(#photo500)"/>
      </svg>
      <div class="brand"><span class="brand__dot"></span><span class="brand__name">voralux</span></div>
      <h1 class="product-name"><span class="product-name__line">SANITARY</span><span class="product-name__line">CLEANER</span></h1>
      <p class="claim">CLEANS, DESCALES &amp; FRESHENS</p>
      <ul class="usp-list">
        <li class="usp"><svg viewBox="0 0 24 24" fill="none" stroke="var(--brand-blue)" stroke-width="1.6"><path d="M8 9h6l1 3v9H7v-9z"/><path d="M9 9V6h4l3-2v3h-3"/></svg><span class="usp__text">Sanitary</span></li>
        <li class="usp"><svg viewBox="0 0 24 24" fill="none" stroke="var(--brand-blue)" stroke-width="1.6"><path d="M5 21V5a2 2 0 0 1 4 0"/><path d="M7 7h5"/><path d="M9 10v1M12 10v2M15 10v1"/></svg><span class="usp__text">Bathroom</span></li>
        <li class="usp"><svg viewBox="0 0 24 24" fill="none" stroke="var(--brand-blue)" stroke-width="1.6"><path d="M7 3h5v8H7z"/><path d="M5 11h14a7 6 0 0 1-7 6h-2v4H8v-4"/></svg><span class="usp__text">Toilet</span></li>
        <li class="usp"><svg viewBox="0 0 24 24" fill="none" stroke="var(--brand-blue)" stroke-width="1.6"><path d="M12 3s6 7 6 11a6 6 0 0 1-12 0c0-4 6-11 6-11z"/></svg><span class="usp__text">Wet areas</span></li>
      </ul>
      <p class="description">Ideal for quick and powerful cleaning. A ready-to-use product for everyday use.</p>
    </article>
  </section>

  <section class="label-slot">
    <p class="label-caption">1L bottle</p>
    <article class="label label--1l">
      <svg class="label__art" viewBox="0 0 100 100" preserveAspectRatio="none" aria-hidden="true">
        <defs>
          <linearGradient id="photo1l" x1="0" y1="0" x2="1" y2="1">
            <stop offset="0" stop-color="#d9dcdf"/><stop offset=".45" stop-color="#f3f4f4"/>
            <stop offset=".75" stop-color="#8d8f92"/><stop offset="1" stop-color="#5a5d62"/>
          </linearGradient>
        </defs>
        <path d="M0 0H100V31Q50 25 0 32Z" fill="var(--brand-blue)"/>
        <path d="M0 58Q50 64 100 57V61Q50 67 0 62Z" fill="var(--mid-blue)"/>
        <path d="M0 57Q50 63 100 56V58Q50 64 0 59Z" fill="var(--soft-blue)"/>
      </svg>
      <svg class="label__art" viewBox="0 0 100 100" preserveAspectRatio="none" role="img" aria-label="Photo of a clean modern bathroom with shower and washbasin">
        <path d="M0 32Q50 25 100 31V56Q50 63 0 57Z" fill="url(#photo1l)"/>
      </svg>
      <div class="brand"><span class="brand__dot"></span><span class="brand__name">voralux</span></div>
      <h1 class="product-name"><span class="product-name__line">SANITARY</span><span class="product-name__line">CLEANER</span></h1>
      <p class="claim">CLEANS, DESCALES &amp; FRESHENS</p>
      <ul class="usp-list">
        <li class="usp"><svg viewBox="0 0 24 24" fill="none" stroke="var(--brand-blue)" stroke-width="1.6"><path d="M8 9h6l1 3v9H7v-9z"/><path d="M9 9V6h4l3-2v3h-3"/></svg><span class="usp__text">Sanitary</span></li>
        <li class="usp"><svg viewBox="0 0 24 24" fill="none" stroke="var(--brand-blue)" stroke-width="1.6"><path d="M5 21V5a2 2 0 0 1 4 0"/><path d="M7 7h5"/><path d="M9 10v1M12 10v2M15 10v1"/></svg><span class="usp__text">Bathroom</span></li>
        <li class="usp"><svg viewBox="0 0 24 24" fill="none" stroke="var(--brand-blue)" stroke-width="1.6"><path d="M7 3h5v8H7z"/><path d="M5 11h14a7 6 0 0 1-7 6h-2v4H8v-4"/></svg><span class="usp__text">Toilet</span></li>
        <li class="usp"><svg viewBox="0 0 24 24" fill="none" stroke="var(--brand-blue)" stroke-width="1.6"><path d="M12 3s6 7 6 11a6 6 0 0 1-12 0c0-4 6-11 6-11z"/></svg><span class="usp__text">Wet areas</span></li>
      </ul>
      <p class="description">Ideal for quick and powerful cleaning. A ready-to-use product for everyday use.</p>
    </article>
  </section>

</main>
</body>
</html>
```